Australia-Wide Industry Leader Bookkeeping Business Website Design Required

We need a website designed for our 10 year old bookkeeping business, Barwick & Lund. Barwick & Lund has been servicing the local & interstate communities of Australia, providing first-class BAS & Bookkeeping services with a personal touch unmatched by anyone else in the county.

What began 10 years ago as a small business focusing on family, friends and the local community, it has since grown into a well respected business with 95% of their business based solely on word of mouth and personal referrals from around Australia.

We would like to see designs that incorporate our existing brand/logo. The colours to be used on the website should be colours that work well with our logo. The design should communicate maturity, trust and confidence with a Web 2.0 look and feel.

We have produced mockups of the entire website as well as assets used in the mockups. Please reference the attached files. The mockups are an example of all the design elements that we want on each page. Designers are encouraged to use the mockups as a guideline only and for designers to use their own creativity.
Updates

This message is for new graphic designers who are considering commencing work on this project. Thank you for expressing an interest in our project. We would like to inform you that this project is close to completion as we have a number designs under very serious consideration.

We are currently in a position where we are disinterested providing feedback to improve on new designs submitted. We will provide feedback to improve new designs only if the submitted designs are very close to what we want for our website, and will only require 1 or 2 revision rounds to refine before the project completion date we will not work with designers to refine their newly submitted designs.

We feel that it is important for all designers to know the above information as we feel that your time and effort may be better spent working on another project.

Thank you for your understanding.

A big thank you for all the designs submitted. We are now in the process of selecting a design. Please be patient during this process. Thank you.

Target Market(s)

Busy Business Owners

Industry/Entity Type

Small Business

Requirements
Must have
• We require a rectangular "slide show" type feature to serve as a "teaser" to arouse the emotions of our website visitors. Each slide asks a specific question. The questions are:

- Is your paperwork in a mess?
- Do you need to get organised for the end of financial year?
- Are you sick & tired of endless amounts of paperwork & BASs?
- Do you feel frustrated & annoyed because you know your books need to be done?
- Do you lack the time & patience to get your paperwork done?
- Do you wish you had more time to do the things you enjoy doing?
- Contact Barwick & Lund today and we will transform your chaos into order.

Underneath the slide show will be a button to "Call Barwick & Lund Now - 03 5550 1827".

```html
<!DOCTYPE html>
<html lang="en">
<head>
<meta charset="utf-8">
<title>Barwick &amp; Lund – Bookkeeping &amp; BAS Services</title>
<link rel="stylesheet" href="https://fonts.googleapis.com/css2?family=Tinos:wght@400;700&display=swap">
<style>
:root{
  --wine:#7d0000;
  --wine-dark:#5e0000;
  --ink:#1b1b1b;
  --grey-band:#dcdadb;
  --grey-hero-top:#d6d4d5;
  --grey-hero-mid:#e8e7e8;
  --nav-dark:#5d5d5f;
  --nav-light:#8a8a8c;
  --footer:#5a595b;
  --white:#ffffff;
  --line:#c9c9c9;
  --map-dark:#3e3e40;
}
*{box-sizing:border-box;margin:0;padding:0}
html,body{width:794px;height:1200px;overflow:hidden}
body{position:relative;font-family:"Tinos","Times New Roman",serif;color:var(--ink);background:var(--white)}
.abs{position:absolute}

/* header band */
.hero-band{left:0;top:0;width:794px;height:395px;
  background:linear-gradient(180deg,var(--grey-hero-top) 0,var(--grey-hero-top) 275px,#58585a 300px,#a9a8aa 330px,var(--grey-hero-mid) 395px)}
.brand{left:290px;top:12px;width:222px;height:43px;background:var(--white);border:1px solid #9a9a9a;
  display:flex;align-items:center;justify-content:center;gap:8px}
.brand-mark{width:10px;height:10px;background:var(--wine)}
.brand-name{font-size:27px;color:var(--wine);font-weight:400;white-space:nowrap}

.main-nav{left:85px;top:80px;width:632px;height:24px;border-radius:4px;
  background:linear-gradient(180deg,var(--nav-light),var(--nav-dark));display:flex;align-items:center}
.main-nav a{font-size:10px;color:#dcdcdc;text-decoration:none;padding:0 7px;height:24px;line-height:24px;border-right:1px solid #4b4b4d}
.main-nav a.current{background:linear-gradient(180deg,#f2f2f2,#d7d7d7);color:var(--ink);padding:0 16px;margin-left:14px;font-weight:700}
.search{margin-left:auto;margin-right:8px;display:flex;align-items:center}
.search span{width:100px;height:15px;background:#f4f4f4;font-size:9px;color:#888;padding:1px 4px;line-height:13px}
.search i{display:block;width:24px;height:15px;background:#dedede;position:relative}
.search i::before{content:"";position:absolute;left:8px;top:3px;width:6px;height:6px;border:1.5px solid #555;border-radius:50%}

.intro{left:80px;top:113px;width:642px;text-align:center;font-size:14.4px;line-height:15px}

.welcome{left:85px;top:162px;width:632px;height:138px;background:var(--wine);border-radius:6px 6px 0 0}
.welcome h1{position:absolute;left:28px;top:10px;font-size:16px;font-weight:400;color:var(--white);text-decoration:underline}
.welcome p{position:absolute;left:28px;top:34px;width:310px;font-size:8.6px;line-height:13.3px;color:var(--white);text-align:justify}
.btn-more{position:absolute;left:27px;top:128px;width:62px;height:17px;background:linear-gradient(180deg,#4a4a4a,#1d1d1d);
  border-radius:3px;color:var(--white);font-size:9px;text-align:center;line-height:17px}
.slide{left:446px;top:176px;width:243px;height:166px;border-radius:3px;overflow:hidden;
  background:linear-gradient(180deg,#f2f2f2 0,#c9c9c9 55%,#8e8e8e 100%)}
.slide-caption{position:absolute;left:0;bottom:0;width:100%;height:30px;background:rgba(60,60,60,.85);
  color:var(--white);font-size:12.5px;font-weight:700;text-align:center;line-height:12px;padding-top:3px}
.slide-nav{left:446px;top:356px;width:243px;height:20px}
.dots{position:absolute;left:78px;top:6px;display:flex;gap:3px}
.dots b{width:9px;height:9px;border:1px solid #555;border-radius:50%;background:#e7e7e7}
.dots b.on{background:var(--wine);border-color:var(--wine)}
.call{left:112px;top:333px;font-size:17.5px;font-weight:700;color:var(--white);line-height:18px}
.call strong{color:var(--ink)}

/* grey section sits under the cards */
.grey-band{left:0;top:607px;width:794px;height:425px;background:var(--grey-band)}

/* summaries */
.card{background:var(--white);border:1px solid var(--line);box-shadow:0 1px 3px rgba(0,0,0,.15)}
.tab{position:absolute;left:-6px;top:12px;height:20px;background:var(--wine);color:var(--white);font-size:12px;line-height:20px;padding:0 12px}
.summary{left:90px;top:416px;width:393px;height:169px}
.summary ul{position:absolute;top:42px;list-style:none;font-size:11px;line-height:19.6px}
.summary ul.a{left:8px}
.summary ul.b{left:200px}
.summary li::before{content:"➤";font-size:9px;margin-right:12px}
.coverage{left:515px;top:416px;width:202px;height:389px}
.coverage .lead{position:absolute;left:8px;top:40px;width:190px;font-size:7.5px;font-weight:700;line-height:10px}
.coverage .big{position:absolute;left:8px;top:71px;width:190px;font-size:12px;line-height:13px}
.map{position:absolute;left:6px;top:102px;width:190px;height:280px;
  background:linear-gradient(180deg,#f7f7f7 0,#f7f7f7 22%,#6a6a6c 38%,var(--map-dark) 52%,#7a7a7c 64%,#f7f7f7 74%,#f7f7f7 100%)}

/* differences */
.diff-title{left:85px;top:619px;font-size:14.5px;font-weight:700;color:var(--wine)}
.checks{left:85px;top:660px;width:400px;list-style:none;font-size:8.6px}
.checks>li{position:relative;padding-left:18px;margin-bottom:15.3px;line-height:13px}
.checks>li::before,.quals li::before{content:"";position:absolute;left:0;top:1px;width:10px;height:10px;background:var(--wine-dark)}
.checks>li::after,.quals li::after{content:"";position:absolute;left:3px;top:2px;width:3px;height:6px;border:solid var(--white);border-width:0 1.5px 1.5px 0;transform:rotate(40deg)}
.sub{list-style:none;margin:4px 0 -4px -16px}
.sub li{position:relative;padding-left:14px;line-height:12px}
.sub li::before{content:"";position:absolute;left:1px;top:3px;width:6px;height:6px;border-radius:50%;background:var(--wine-dark)}
.diff-close{left:85px;top:1005px;font-size:14.5px;font-weight:700;color:var(--wine)}
.quals-title{left:515px;top:834px;font-size:11px;font-weight:700;color:var(--wine)}
.quals{left:515px;top:862px;width:200px;list-style:none;font-size:10.2px}
.quals li{position:relative;padding-left:23px;line-height:16px}
.quals li::before{top:3px}
.quals li::after{left:4px;top:4px}

/* partners */
.partners{left:0;top:1032px;width:794px;height:117px;background:var(--white)}
.badge{position:absolute;background:#c8c8c8}
.footer{left:0;top:1149px;width:794px;height:51px;background:var(--footer);color:var(--white);font-size:9px}
.follow{position:absolute;left:85px;top:18px;display:flex;align-items:center;gap:6px}
.follow i{display:block;width:19px;height:19px;border-radius:50%;background:#3c3c3d}
.follow i.alt{background:var(--wine)}
.copy{position:absolute;right:77px;top:24px;font-size:8.5px}
</style>
</head>
<body>

<div class="abs hero-band"></div>
<div class="abs grey-band"></div>

<div class="abs brand"><span class="brand-mark"></span><span class="brand-name">Barwick &amp; Lund</span></div>

<nav class="abs main-nav">
  <a class="current">Home</a><a>About us</a><a>Services</a><a>Testimonials</a><a>Articles</a><a>Endorsements</a><a>Links</a><a>Contact us</a>
  <div class="search"><span>Search</span><i></i></div>
</nav>

<p class="abs intro">For nearly 10 years barwick &amp; lund has been servicing the local &amp; interstate communities of Australia, providing first - class bas &amp; book keeping services with a personal touch unmatched by anyone else in the country.</p>

<section class="abs welcome">
  <h1>Welcome to Barwick &amp; Lund</h1>
  <p>Having worked for a certified accountant firm for numerous year, Helen Barwick &amp; Joanne Lund become concerned about the consistency of inaccurate books prepared by other in various organization. As the quality of bookworm declined, the fees seemed to increased , together they identified a need for a quality bookkeeping that truly understood what being is business is all about &amp; more importantly how to correctly &amp; accurately process book according to the los &amp; requirement set by the Australian taxation office.</p>
  <span class="btn-more">Learn More</span>
</section>

<div class="abs slide" role="img" aria-label="Photo of a hand holding up a small help flag above a pile of paperwork">
  <div class="slide-caption">Contact Barwick &amp; Lund today and we<br>will transform your chaos into order ?</div>
</div>

<div class="abs call">"Call Barwick &amp; Lund<br>Now - <strong>03 5550 1827</strong>"
  <svg width="26" height="30" viewBox="0 0 26 30" style="vertical-align:-6px"><path d="M6 3c2-1 4 0 5 2l1 4c0 1-1 2-2 3 1 3 3 6 6 8 1-1 2-2 3-2l4 1c2 1 2 3 1 5-2 3-6 3-10 0-5-4-9-9-10-14C3 7 4 4 6 3z" fill="#b00000"/></svg>
</div>

<div class="abs slide-nav">
  <svg class="abs" style="left:0;top:0" width="20" height="20" viewBox="0 0 20 20"><path d="M17 3 4 10l13 7" fill="none" stroke="#2a2a2a" stroke-width="3"/></svg>
  <div class="dots"><b></b><b></b><b></b><b class="on"></b><b></b><b></b><b></b></div>
  <svg class="abs" style="right:0;top:0" width="20" height="20" viewBox="0 0 20 20"><path d="M3 3l13 7-13 7" fill="none" stroke="#2a2a2a" stroke-width="3"/></svg>
</div>

<section class="abs card summary">
  <span class="tab">To Summaries</span>
  <ul class="a">
    <li>Free initial consulting</li><li>Bookkeeping</li><li>Pay roll</li><li>Superannuation</li><li>Fuel tax credit</li><li>Ledgerline software &amp; training</li>
  </ul>
  <ul class="b">
    <li>Register BAS agent #41826-053</li><li>BAS preparation &amp; lodgment</li><li>IAS preparation &amp; lodgment</li><li>Margined scheme</li><li>Offsite &amp; onsite bookkeeping</li><li>Australian wide</li>
  </ul>
</section>

<section class="abs card coverage">
  <span class="tab">Service all of Australia</span>
  <p class="lead">95% of our clients come from client &amp; accountant referrals. We have client all over Victoria Queensland, NSW &amp; Western Australia</p>
  <p class="big">so no matter where you are we can help</p>
  <div class="map" role="img" aria-label="Map of Australia marking client locations by state, with town lists for each state"></div>
</section>

<h2 class="abs diff-title">What makes Barwick &amp; Lund different from other bookkeepers</h2>
<ul class="abs checks">
  <li>We guarantee we quality of our work</li>
  <li>We have owned a operated business for 35 years</li>
  <li>We have over 35 years of experienced</li>
  <li>The Barwick &amp; Lund team are investors &amp; traders</li>
  <li>Extensive business network for your benefits</li>
  <li>Backed by a team of accountants</li>
  <li>We work with a team of elite accountants &amp; wealth Creation professionals who coach us monthly in the following:
    <ul class="sub"><li>Assets protection</li><li>superannuation &amp; self managed<br>superannuationfunds</li><li>property investing</li><li>tax steatites, tax structure &amp; best tax saving</li></ul>
  </li>
  <li>We understand just how important it is to help lead &amp; guide our clients from making profits to:
    <ul class="sub"><li>Maximum profits</li><li>Wealth creation</li><li>Tax minim station</li><li>Asset protection</li></ul>
  </li>
</ul>
<p class="abs diff-close">This is something that other bookkeeper just don’t do !</p>

<h2 class="abs quals-title">Qualifications, Membership &amp; Partnership</h2>
<ul class="abs quals">
  <li>Register ATO BAS agent</li>
  <li>Certified IV financial service</li>
  <li>Certified III financial services</li>
  <li>Member of institute of registered bookkeepers</li>
  <li>Platinum member of Australian bookkeepers</li>
  <li>Ledgerline professional partner</li>
  <li>Tax Wise Network</li>
</ul>

<section class="abs partners" aria-label="Partner and membership badges">
  <span class="badge" style="left:85px;top:16px;width:47px;height:80px"></span>
  <span class="badge" style="left:204px;top:16px;width:72px;height:80px"></span>
  <span class="badge" style="left:336px;top:26px;width:90px;height:72px"></span>
  <span class="badge" style="left:486px;top:34px;width:32px;height:60px"></span>
  <span class="badge" style="left:563px;top:42px;width:154px;height:38px"></span>
</section>

<footer class="abs footer">
  <div class="follow">FOLLOW US ON <i></i><i class="alt"></i></div>
  <p class="copy">© Copyrights 2012 Barwick &amp; Lund</p>
</footer>

</body>
</html>
```